Maple Lantern Business Card

Design of business cards

Target Market(s)

We are aiming as small business owners who need anything from basic business structures, website plans, business processes and quality assurance.

Industry/Entity Type

Business

Colors

Designer to choose colors to be used in the design.

Requirements
Nice to have
• I would prefer one side of the card to use the green from the logo. Prefer to have the same font as the logo.

```html
<!DOCTYPE html>
<html lang="en">
<head>
<meta charset="utf-8">
<title>Maple Lantern Consulting – Business Card</title>
<link rel="stylesheet" href="https://fonts.googleapis.com/css2?family=Marcellus+SC&family=Tinos:wght@400;700&display=swap">
<style>
  :root {
    --bg: #d9dbdc;
    --card-white: #ffffff;
    --charcoal: #323232;
    --green: #a2cd3a;
    --green-dark: #78a332;
    --green-light: #cfe37d;
    --green-pale: #e6f0b4;
    --grey-light: #e6e7e8;
    --grey-mid: #cfd1d2;
  }
  html, body {
    margin: 0;
    width: 1200px;
    height: 1000px;
    overflow: hidden;
    background: var(--bg);
  }
  .sheet {
    position: relative;
    width: 1200px;
    height: 1000px;
  }
  .card {
    position: absolute;
    left: 250px;
    width: 700px;
    height: 400px;
    box-shadow: 0 6px 18px rgba(0,0,0,0.18);
  }
  .card--front { top: 70px; }
  .card--back { top: 530px; }
  .brand-name {
    font-family: "Marcellus SC", serif;
    fill: var(--charcoal);
  }
  .contact-line {
    font-family: "Tinos", serif;
    font-size: 17px;
  }
  .role-title {
    font-family: "Tinos", serif;
    font-size: 22px;
    fill: var(--green);
  }
  .person-name {
    font-family: "Tinos", serif;
    font-weight: 700;
    font-size: 32px;
    fill: var(--card-white);
    letter-spacing: 1px;
  }
</style>
</head>
<body>
<main class="sheet">

  <!-- Front of card -->
  <svg class="card card--front" viewBox="0 0 700 400" xmlns="http://www.w3.org/2000/svg">
    <rect width="700" height="400" fill="var(--card-white)"/>

    <!-- top segmented band -->
    <g class="top-band">
      <polygon points="110,0 260,0 245,22 95,22" fill="var(--grey-light)"/>
      <polygon points="262,0 420,0 405,22 247,22" fill="var(--green-dark)"/>
      <polygon points="422,0 560,0 545,22 407,22" fill="var(--green)"/>
      <polygon points="562,0 640,0 625,22 547,22" fill="var(--green-light)"/>
      <polygon points="642,0 700,0 700,22 627,22" fill="var(--green-pale)"/>
    </g>

    <!-- brand -->
    <circle class="brand-mark" cx="120" cy="140" r="46" fill="var(--green)"/>
    <text class="brand-name" x="190" y="102" font-size="34">Maple</text>
    <text class="brand-name" x="190" y="142" font-size="34">Lantern</text>
    <text class="brand-name" x="190" y="182" font-size="34">Consulting</text>

    <!-- contact rows -->
    <g class="contact">
      <polygon points="320,206 700,206 700,238 300,238" fill="var(--green)"/>
      <text class="contact-line" x="600" y="228" text-anchor="end" fill="var(--card-white)">ninth street, Oakridge-2210</text>
      <polygon points="300,242 700,242 700,274 280,274" fill="var(--grey-light)"/>
      <text class="contact-line" x="600" y="264" text-anchor="end" fill="var(--charcoal)">maplelantern@mail.com</text>
      <polygon points="280,278 700,278 700,310 260,310" fill="var(--grey-light)"/>
      <text class="contact-line" x="600" y="300" text-anchor="end" fill="var(--charcoal)">000-2847-3316, 000-2847-3316</text>

      <!-- pin icon -->
      <path d="M640,212 a8,8 0 0 1 8,8 c0,6 -8,14 -8,14 c0,0 -8,-8 -8,-14 a8,8 0 0 1 8,-8z" fill="var(--charcoal)"/>
      <circle cx="640" cy="220" r="3" fill="var(--green)"/>
      <!-- mail icon -->
      <rect x="628" y="250" width="24" height="16" fill="var(--charcoal)"/>
      <polyline points="628,250 640,260 652,250" fill="none" stroke="var(--grey-light)" stroke-width="1.5"/>
      <!-- phone icon -->
      <path d="M629,300 h22 l-3,-10 h-4 v-3 h-8 v3 h-4z" fill="var(--charcoal)"/>
      <rect x="630" y="301" width="20" height="4" fill="var(--charcoal)"/>
    </g>

    <!-- bottom band -->
    <rect x="0" y="318" width="700" height="8" fill="var(--green)"/>
    <polygon points="0,326 300,326 350,400 0,400" fill="var(--charcoal)"/>
    <polygon points="352,326 480,326 480,400 402,400" fill="var(--grey-light)"/>
    <polygon points="480,326 590,326 590,400 480,400" fill="var(--green-light)"/>
    <polygon points="590,326 700,326 700,400 590,400" fill="var(--green)"/>
    <text class="role-title" x="30" y="356">Executive Director</text>
    <text class="person-name" x="30" y="390">NAME</text>
  </svg>

  <!-- Back of card -->
  <svg class="card card--back" viewBox="0 0 700 400" xmlns="http://www.w3.org/2000/svg">
    <rect width="700" height="400" fill="var(--green)"/>
    <rect x="0" y="0" width="700" height="85" fill="var(--charcoal)"/>
    <rect x="0" y="315" width="700" height="85" fill="var(--charcoal)"/>

    <g class="top-segments">
      <polygon points="200,0 330,0 320,26 190,26" fill="var(--grey-light)"/>
      <polygon points="332,0 460,0 450,26 322,26" fill="var(--green-dark)"/>
      <polygon points="462,0 560,0 550,26 452,26" fill="var(--green)"/>
      <polygon points="562,0 640,0 630,26 552,26" fill="var(--green-light)"/>
      <polygon points="642,0 700,0 700,26 632,26" fill="var(--green-pale)"/>
    </g>
    <g class="bottom-segments">
      <polygon points="0,374 80,374 88,400 0,400" fill="var(--green-light)"/>
      <polygon points="82,374 250,374 258,400 90,400" fill="var(--green)"/>
      <polygon points="252,374 400,374 408,400 260,400" fill="var(--green-dark)"/>
      <polygon points="402,374 520,374 528,400 410,400" fill="var(--grey-light)"/>
    </g>

    <circle class="brand-mark" cx="140" cy="200" r="58" fill="var(--charcoal)"/>
    <text class="brand-name" x="240" y="158" font-size="40">Maple</text>
    <text class="brand-name" x="240" y="208" font-size="40">Lantern</text>
    <text class="brand-name" x="240" y="258" font-size="40">Consulting</text>
  </svg>

</main>
</body>
</html>
```